Web Design for a Biotech Consulting Firm

We need a web site design for a new business based in Philadelphia called VorentaMx. This is a consulting firm that will serve medical diagnostics industry, which is part of the life science/healthcare industry focusing on developing and marketing products that help in early detection, monitoring or management of diseases. Our consulting firm will help medical diagnostic companies to overcome key challenges in designing, evaluating and marketing new products.Our company name is VorentaMx. Vorenta is Latin word for "something" Dx represents diagnostics. The idea behind the name is that we help companies to transform the original, early product ideas ("nothing") into "something"; which is a product with full clinical utility that will help to improve health and well-being.The web site should use the visual feel of the logo (attached), be modern, simple and clean looking and represent creativity, innovation, scientific thinking and progress.
Updates

Wix Design is acceptable

Industry/Entity Type

Biotechnology

Coding

Coded - Design and coding required

Number of Pages Required

1 page

Font styles to use
Sans Serif

Requirements
Must have
• simple, clean look couple of pages
Should not have
• a lot of pages

```html
<!DOCTYPE html>
<html lang="en">
<head>
<meta charset="utf-8">
<title>Vorenta Mx — Medical Diagnostics Consulting</title>
<link href="https://fonts.googleapis.com/css2?family=Montserrat:wght@400;500;600&family=Playfair+Display:wght@700&display=swap" rel="stylesheet">
<style>
:root{
  --blue:#1e86f5;
  --ink:#222;
  --muted:#8a8a8a;
  --dark:#2b2b2b;
  --black:#0c0c0c;
  --band:#f3f3f3;
  --white:#fff;
}
*{box-sizing:border-box;margin:0;padding:0}
html,body{width:1200px;height:2990px;overflow:hidden}
body{font-family:'Montserrat',sans-serif;color:var(--ink);background:var(--white);position:relative}
.serif{font-family:'Playfair Display',serif;font-weight:700}
.abs{position:absolute}
.topbar{left:0;top:0;width:1200px;height:52px;background:var(--blue)}
.topbar .item{top:0;height:52px;display:flex;align-items:center;gap:12px;color:#fff;font-size:14px;font-weight:500;padding:0 22px;border-left:1px solid rgba(255,255,255,.3)}
.brand{display:flex;align-items:center;gap:10px;font-size:18px;font-weight:500;white-space:nowrap}
.brand .mark{width:14px;height:14px;background:var(--blue)}
.nav{top:52px;height:93px;left:330px;display:flex;align-items:center;gap:48px;font-size:15px;color:#444}
.nav .on{color:var(--blue);font-weight:500}
.search{left:831px;top:78px;width:292px;height:41px;border:1px solid #ddd;border-radius:21px;display:flex;align-items:center;justify-content:space-between;padding:0 14px 0 20px;font-size:14px;font-style:italic;color:#999}
.hero{left:0;top:145px;width:1200px;height:573px;background:linear-gradient(100deg,#5c7da0 0%,#8fb0cf 40%,#c7d6e3 70%,#9bb3c8 100%)}
.hero-title{left:77px;top:260px;width:438px;height:104px;background:rgba(30,134,245,.9);color:#fff;font-size:74px;padding-left:23px;line-height:104px;white-space:nowrap}
.hero-sub{left:77px;top:385px;width:490px;height:136px;background:rgba(40,40,40,.8);color:#fff;font-size:48px;line-height:52px;padding:14px 0 0 23px}
.btn{border-radius:26px;color:#fff;font-size:18px;font-weight:500;display:flex;align-items:center;justify-content:center}
.btn-blue{background:var(--blue)}
.btn-dark{background:var(--dark)}
.section-title{left:0;width:1200px;text-align:center;font-size:44px;color:var(--ink)}
.section-title em{font-style:normal;color:var(--blue)}
.lede{left:270px;width:660px;top:840px;text-align:center;font-size:14px;line-height:26px;color:var(--muted)}
.band{left:0;top:1145px;width:1200px;height:345px;background:var(--band)}
.card{top:926px;width:334px;height:500px;background:#fff;box-shadow:0 0 6px rgba(0,0,0,.15);text-align:center}
.card .photo{width:334px;height:219px}
.card .badge{position:absolute;left:122px;top:174px;width:90px;height:90px;border-radius:50%;background:var(--blue);border:5px solid #d6e8fd;display:flex;align-items:center;justify-content:center}
.card h3{margin-top:72px;font-size:22px;font-weight:500}
.card p{margin:18px 24px 0;font-size:14px;line-height:26px;color:var(--muted)}
.card a{display:inline-block;margin-top:12px;color:var(--blue);font-size:15px;font-weight:500;padding-bottom:8px;border-bottom:1px solid #a9cdf8}
.split-photo{left:0;top:1490px;width:600px;height:468px;background:linear-gradient(120deg,#cfd6cc,#9fb7a9 45%,#e4e6e2)}
.split-text{left:600px;top:1490px;width:600px;height:468px;background:var(--blue);color:#fff;padding:55px 0 0 54px}
.split-text h2{font-size:44px}
.split-text p{margin-top:22px;width:456px;font-size:14px;line-height:26px}
.news{top:2104px;width:251px}
.news .photo{height:167px}
.news h4{margin:18px 2px 0;font-size:17px;font-weight:500;line-height:27px;color:#333}
.news time{display:block;margin:10px 2px 0;font-size:14px;color:#777}
.cta{left:0;top:2438px;width:1200px;height:260px;background:linear-gradient(100deg,#2b85ef,#4b9af3 50%,#2a84ef)}
.cta p{position:absolute;left:0;width:1200px;top:55px;text-align:center;color:#fff;font-size:26px;line-height:37px;font-weight:500}
.footer{left:0;top:2698px;width:1200px;height:207px;background:var(--black);color:#fff}
.copy{left:0;top:2905px;width:1200px;height:85px;background:var(--black);border-top:1px solid #222;color:#ccc;font-size:13px;text-align:center;line-height:85px}
.circ{width:50px;height:50px;border-radius:50%;background:#fff;display:flex;align-items:center;justify-content:center}
.social{width:47px;height:47px;border-radius:50%;background:#fff}
</style>
</head>
<body>

<div class="abs topbar">
  <div class="abs item" style="left:724px">
    <svg width="22" height="22" viewBox="0 0 24 24" fill="none" stroke="#fff" stroke-width="1.6"><path d="M5 3h4l2 5-3 2a12 12 0 0 0 6 6l2-3 5 2v4a2 2 0 0 1-2 2A17 17 0 0 1 3 5a2 2 0 0 1 2-2z"/></svg>
    123.456.7890
  </div>
  <div class="abs item" style="left:906px;border-right:1px solid rgba(255,255,255,.3)">
    <svg width="20" height="16" viewBox="0 0 20 16" fill="none" stroke="#fff" stroke-width="1.6"><rect x="1" y="1" width="18" height="14"/><path d="M1 1l9 8 9-8"/></svg>
    info@vorentamx.com
  </div>
</div>

<div class="abs brand" style="left:77px;top:67px;color:var(--ink)"><span class="mark"></span>Vorenta Mx</div>
<nav class="abs nav"><span class="on">Home</span><span>About</span><span>Services</span><span>News</span><span>Contact</span></nav>
<div class="abs search">Search here......
  <svg width="22" height="22" viewBox="0 0 24 24" fill="none" stroke="#1e86f5" stroke-width="2"><circle cx="10" cy="10" r="7"/><path d="M15 15l6 6"/></svg>
</div>

<div class="abs hero" role="img" aria-label="Photo of three doctors reviewing a tablet in a bright modern clinic"></div>
<div class="abs hero-title serif">Vorenta Mx</div>
<div class="abs hero-sub serif">Medical Diagnostics Consulting</div>
<div class="abs btn btn-blue" style="left:78px;top:546px;width:146px;height:52px">Read More</div>

<h2 class="abs section-title serif" style="top:772px">What <em>We Offers</em></h2>
<p class="abs lede">Lorem ipsum dolor sit amet, consectetur adipiscing elit, sed do eiusmod tempor incididunt ullamco laboris nisi ut aliquip ex ea commodo consequat.</p>

<div class="abs band"></div>

<div class="abs card" style="left:77px">
  <div class="photo" role="img" aria-label="Photo of a couple meeting a doctor at a desk" style="background:linear-gradient(120deg,#c9c2b8,#e7e4df 50%,#a9a39c)"></div>
  <div class="badge"><svg width="44" height="44" viewBox="0 0 44 44" fill="none" stroke="#fff" stroke-width="2"><rect x="6" y="8" width="32" height="22" rx="2"/><path d="M2 34h40M22 12l7 3v5c0 4-3 6-7 7-4-1-7-3-7-7v-5z"/></svg></div>
  <h3>Developement</h3>
  <p>Lorem ipsum dol consectetur adipiscing elit, sed do eiusmod tempor incididunt ut labore et dolore magna aliqua.</p>
  <a>Read More</a>
</div>
<div class="abs card" style="left:433px">
  <div class="photo" role="img" aria-label="Photo of a nurse caring for an elderly woman" style="background:linear-gradient(120deg,#d9d4cc,#c24a4a 60%,#e5ddd0)"></div>
  <div class="badge"><svg width="44" height="44" viewBox="0 0 44 44" fill="none" stroke="#fff" stroke-width="2"><rect x="6" y="6" width="32" height="32" rx="2"/><circle cx="22" cy="18" r="7"/><path d="M15 18h14M22 11v14M12 30h20M12 34h20"/></svg></div>
  <h3>Marketing</h3>
  <p>Lorem ipsum dol consectetur adipiscing elit, sed do eiusmod tempor incididunt ut labore et dolore magna aliqua.</p>
  <a>Read More</a>
</div>
<div class="abs card" style="left:789px">
  <div class="photo" role="img" aria-label="Photo of a medical team meeting around a table" style="background:linear-gradient(120deg,#b9c3c9,#e3e6e6 50%,#8e9aa4)"></div>
  <div class="badge"><svg width="44" height="44" viewBox="0 0 44 44" fill="none" stroke="#fff" stroke-width="2"><rect x="8" y="6" width="20" height="32" rx="2"/><circle cx="18" cy="22" r="5"/><path d="M12 12h12M32 10v28M38 10v28M30 14h4M36 14h4"/></svg></div>
  <h3>Monitoring</h3>
  <p>Lorem ipsum dol consectetur adipiscing elit, sed do eiusmod tempor incididunt ut labore et dolore magna aliqua.</p>
  <a>Read More</a>
</div>

<div class="abs split-photo" role="img" aria-label="Photo of a senior doctor reviewing notes with a smiling patient"></div>
<div class="abs split-text">
  <h2 class="serif">What We Offers</h2>
  <p>Lorem ipsum dolor sit amet, consectetur adipiscing elit, sed do eiusmod tempor incididunt ut labore et dolore magna aliqua. Ut enim ad minim veniam, quis nostrud exercitation ullamco laboris nisi ut aliquip ex ea commodo consequat. Duis aute irure dolor in reprehenderit in voluptate velit esse cillum dolore eu fugiat nulla pariatur. Excepteur sint occaecat cupidatat non proident, sunt in culpa qui officia deserunt mollit anim id est laborum. But I must explain to you how all this mistaken idea of denouncing.</p>
  <div class="btn btn-dark" style="margin:20px 0 0 -2px;width:146px;height:52px">Read More</div>
</div>

<h2 class="abs section-title serif" style="top:2012px">Latest <em>News Update</em></h2>
<article class="abs news" style="left:77px"><div class="photo" role="img" aria-label="Photo of a nurse with a patient in a wheelchair" style="background:linear-gradient(120deg,#cfe0e6,#7fc6c9 50%,#dfe6ea)"></div><h4>Lorem ipsum dolor sit amet, magna aliqua.</h4><time>17 June 2019</time></article>
<article class="abs news" style="left:342px"><div class="photo" role="img" aria-label="Photo of doctors talking in a hospital corridor" style="background:linear-gradient(120deg,#8fa9b6,#d7d9d2 50%,#b99a72)"></div><h4>Lorem ipsum dolor sit amet, magna aliqua.</h4><time>17 June 2019</time></article>
<article class="abs news" style="left:607px"><div class="photo" role="img" aria-label="Photo of young doctors reviewing a clipboard" style="background:linear-gradient(120deg,#e4e9ee,#7aaed6 50%,#f0f2f4)"></div><h4>Lorem ipsum dolor sit amet, magna aliqua.</h4><time>17 June 2019</time></article>
<article class="abs news" style="left:872px"><div class="photo" role="img" aria-label="Photo of a doctor consulting patients in a waiting area" style="background:linear-gradient(120deg,#9aa7ad,#d6d8d4 50%,#7fa7a6)"></div><h4>Lorem ipsum dolor sit amet, magna aliqua.</h4><time>17 June 2019</time></article>

<section class="abs cta" role="img" aria-label="Blue-tinted background photo of a stethoscope on a keyboard">
  <p>Want to learn more about Us?<br>Get in touch with us for Vorenta Services.</p>
  <div class="abs btn btn-dark" style="left:522px;top:146px;width:156px;height:52px">Contact Us</div>
</section>

<footer class="abs footer">
  <div class="abs brand" style="left:77px;top:82px;color:#fff;font-size:17px"><span class="mark"></span>Vorenta Mx</div>
  <div class="abs" style="left:198px;top:58px;width:108px;font-size:14px;line-height:26px;text-align:center">Lorem dolor sit<br>am consectetur<br>labore&nbsp; dolore<br><span style="text-decoration:underline">Read more</span></div>
  <div class="abs circ" style="left:346px;top:86px"><svg width="22" height="22" viewBox="0 0 24 24" fill="#1e86f5"><path d="M12 3l10 9h-3v9h-5v-6h-4v6H5v-9H2z"/></svg></div>
  <div class="abs" style="left:413px;top:84px;font-size:14px;line-height:26px">123, Address, State Name,<br>City Name,Zipcode</div>
  <div class="abs circ" style="left:615px;top:86px"><svg width="22" height="22" viewBox="0 0 24 24" fill="#1e86f5"><path d="M5 3h4l2 5-3 2a12 12 0 0 0 6 6l2-3 5 2v4a2 2 0 0 1-2 2A17 17 0 0 1 3 5a2 2 0 0 1 2-2z"/></svg></div>
  <div class="abs" style="left:684px;top:84px;font-size:14px;line-height:26px">123.456.7890<br>info@vorentamx.com</div>
  <div class="abs social" style="left:883px;top:87px;background:var(--blue)"></div>
  <div class="abs social" style="left:935px;top:87px"></div>
  <div class="abs social" style="left:987px;top:87px"></div>
  <div class="abs social" style="left:1039px;top:87px"></div>
</footer>
<div class="abs copy">Copyright © Vorenta Mx - 2019 . All Right Reserved</div>

</body>
</html>
```